Business Card Design

We need a business card design for a new company based in Allen, Texas. (outside of Dallas,Texas) We offer Business Management Solutions to Entrepreneurs, as well as Corporate Businesses. Our product line offers solutions to Image, Branding, Social Media marketing, business development strategies, banking / funding solutions, just to name a few. We would like to see designs that convey strength and confidence. I have attached a sample design of our company name. Designers you may use company name as either: Tovan or Tovan Corporation, depending on the design layout.

Please show alternate color of Black as well.

Industry/Entity Type

Business

Contact Information for Business Card

Tovan Corporation

4862 N. Brisbury Lane, STE 300
Marlow Springs, TX 75422
Office: 512.638.4471
Fax: 512.638.4472

Dr. Louis Brennick
Business Development Director

```html
<!DOCTYPE html>
<html lang="en">
<head>
<meta charset="utf-8">
<title>Tovan Business Card</title>
<link rel="stylesheet" href="https://fonts.googleapis.com/css2?family=Open+Sans:wght@300;400&display=swap">
<style>
  :root {
    --backdrop: #6c7686;
    --card-dark: #333333;
    --card-light: #f2f2f2;
    --ink-light: #ffffff;
    --ink-dark: #2f2f2f;
    --ink-muted: #555555;
  }
  * { margin: 0; padding: 0; box-sizing: border-box; }
  html, body {
    width: 1200px; height: 1024px; overflow: hidden;
    background: var(--backdrop);
    font-family: "Open Sans", sans-serif;
  }
  .stage { position: relative; width: 1200px; height: 1024px; }
  .card {
    position: absolute;
    width: 600px; height: 343px;
    box-shadow: 0 18px 40px rgba(0,0,0,0.3);
  }
  .card--front {
    left: 90px; top: 140px;
    background: var(--card-dark);
    color: var(--ink-light);
  }
  .card--back {
    left: 510px; top: 540px;
    background: var(--card-light);
    color: var(--ink-dark);
    border-left: 14px solid var(--card-dark);
  }
  .wordmark {
    position: absolute;
    font-weight: 300;
    letter-spacing: 2px;
    line-height: 1;
  }
  .card--front .wordmark {
    font-size: 104px;
    left: 0; right: 0; top: 96px;
    text-align: center;
  }
  .card--front .website {
    position: absolute;
    right: 70px; top: 248px;
    font-size: 17px;
    font-weight: 400;
  }
  .card--back .wordmark {
    font-size: 84px;
    left: 50px; top: 48px;
    color: var(--ink-dark);
  }
  .person {
    position: absolute;
    left: 330px; top: 150px;
  }
  .person__name { font-size: 22px; font-weight: 400; }
  .person__title { font-size: 12px; color: var(--ink-muted); }
  .contact {
    position: absolute;
    left: 330px; top: 215px;
    font-size: 13px;
    line-height: 1.55;
    list-style: none;
  }
  .contact__address { margin-bottom: 6px; }
  .contact__item { display: flex; align-items: center; gap: 7px; }
  .contact__item svg { width: 11px; height: 11px; fill: var(--ink-dark); }
</style>
</head>
<body>
<main class="stage">
  <section class="card card--front" aria-label="Card front">
    <div class="wordmark">tovan</div>
    <div class="website">www.tovanweb.com</div>
  </section>

  <section class="card card--back" aria-label="Card back">
    <div class="wordmark">tovan</div>
    <div class="person">
      <div class="person__name">Your Name</div>
      <div class="person__title">Title</div>
    </div>
    <ul class="contact">
      <li class="contact__address">4862 N. Brisbury Lane,<br>STE 300 Marlow Springs, TX 75422</li>
      <li class="contact__item">
        <svg viewBox="0 0 12 12" aria-hidden="true"><path d="M2.5 1l2 2.2-1 1.3a6 6 0 0 0 4 4l1.3-1 2.2 2-1.2 1.5C5 11 1 7 1 2.2z"/></svg>
        512.638.4471
      </li>
      <li class="contact__item">
        <svg viewBox="0 0 12 12" aria-hidden="true"><rect x="3" y="1" width="6" height="3"/><rect x="1" y="4.5" width="10" height="5" rx="1"/><rect x="3" y="8" width="6" height="3"/></svg>
        512.638.4472
      </li>
      <li class="contact__item">
        <svg viewBox="0 0 12 12" aria-hidden="true"><circle cx="6" cy="6" r="5"/></svg>
        www.tovanweb.com
      </li>
    </ul>
  </section>
</main>
</body>
</html>
```